Need Business Card Design, Letterhead and a Basic Form layout based on Existing Logo

We need (1) a business card design, (2) a letterhead design and (3) a basic form layout for an international holding company. This holding company has just formed two (2) sub-companies. The logo is the same for each company with only a simple word change for each company. The business card, letterhead and form design will be essentially the same for each company... with only the one word change being different.
The names of the companies are as follows:
1. Halvorn Trust Services
2. Halvorn Immigration Services
The design for the business card, letterhead and Form must be strong, clean and classy.
Our clients will be older, wealthy and mostly Asian. The design must project strength, stability and confidence.
The card may contain the following data:
1. The Logo
2. The name of the person
3. The title of the person
4. The address of the company
5. The Company Phone number
6. The personal mobile number
7. The Skype number (VOIP)
8. The WICKR number (IM)
9. The email
10. The website
We will attach AI files of our logo for the "Halvorn Trust Services" company in the colors Black/White and Blue in both Horizontal and Vertical format... We have also included separate files of the logo icon.
We uploaded the AI files to give the designer the maximum options regarding color and effects. We included the separate files for the icon because we would like to give the designer the option of a watermark. Also, we think it might be nice to highlight the icon on the back of the card perhaps with the website address.
We are not sure which colors or color combinations would be best for these two companies. We know the colors must again project strength, stability and confidence. Perhaps, a combination that might include Tan, Black and White... not sure... need design help... remember this has to have the presence of a bank-like institution... no cartoonish designs or flashy color combinations... please.
The basic form layout will be used for various questionaires, input sheets and instructions.... etc.
NOTE: The fonts used in the logo are Trajan Pro Bold for word "HALVORN" and Trajan Pro Regular for "XXXXXXXXX SERVICES".

```html
<!DOCTYPE html>
<html lang="en">
<head>
<meta charset="utf-8">
<title>Halvorn Trust Services – Business Card</title>
<link href="https://fonts.googleapis.com/css2?family=Cinzel:wght@400;700&family=Open+Sans:wght@400;600&display=swap" rel="stylesheet">
<style>
  :root {
    --backdrop: #e8e5df;
    --card-white: #ffffff;
    --card-black: #1c1c1c;
    --ink: #1a1a1a;
    --ink-soft: #3a3a3a;
    --rule: #9a9a9a;
    --on-dark: #f4f4f4;
  }
  * { margin: 0; padding: 0; box-sizing: border-box; }
  html, body {
    width: 1200px; height: 720px; overflow: hidden;
    background: var(--backdrop);
  }
  .canvas {
    position: relative; width: 1200px; height: 720px;
  }
  .card {
    position: absolute; top: 205px;
    width: 540px; height: 310px;
    box-shadow: 0 6px 18px rgba(0,0,0,0.18);
    overflow: hidden;
  }
  .card-front { left: 40px; background: var(--card-white); }
  .card-back  { left: 620px; background: var(--card-black); }

  .front-corner { position: absolute; inset: 0; }

  .holder {
    position: absolute; top: 12px; right: 40px;
    text-align: right; color: var(--on-dark);
    font-family: "Cinzel", serif;
  }
  .holder-name { font-size: 17px; letter-spacing: 0.5px; line-height: 1.1; }
  .holder-title { font-size: 10px; letter-spacing: 0.8px; }

  .brand {
    position: absolute; left: 58px; top: 118px;
    display: flex; align-items: center; gap: 16px;
    color: var(--ink);
    font-family: "Cinzel", serif;
  }
  .brand-square {
    width: 52px; height: 52px; background: var(--ink);
    transform: rotate(45deg);
  }
  .brand-name { font-size: 31px; font-weight: 700; letter-spacing: 1px; line-height: 1; }
  .brand-division { font-size: 15px; font-weight: 400; letter-spacing: 0.8px; margin-top: 2px; }

  .contacts {
    position: absolute; left: 18px; top: 226px;
    list-style: none;
    font-family: "Open Sans", sans-serif; font-size: 11.5px;
    color: var(--ink-soft); line-height: 13.5px;
  }
  .contacts li { display: flex; align-items: center; gap: 6px; }
  .contact-icon { width: 9px; height: 9px; flex: none; }

  .address {
    position: absolute; left: 250px; top: 226px;
    padding-left: 9px; border-left: 1px solid var(--rule);
    font-family: "Open Sans", sans-serif; font-size: 11.5px;
    color: var(--ink-soft); line-height: 13.5px;
  }

  .back-brand {
    position: absolute; left: 0; right: 0; top: 92px;
    display: flex; justify-content: center; align-items: center; gap: 18px;
    color: var(--on-dark);
    font-family: "Cinzel", serif; font-size: 38px; font-weight: 700; letter-spacing: 2px;
  }
  .back-square {
    width: 46px; height: 46px; background: var(--on-dark);
    transform: rotate(45deg);
  }
  .back-web {
    position: absolute; left: 0; right: 0; top: 228px;
    text-align: center; color: var(--on-dark);
    font-family: "Open Sans", sans-serif; font-size: 15px; letter-spacing: 3px;
  }
</style>
</head>
<body>
<main class="canvas">

  <section class="card card-front" aria-label="Business card front">
    <svg class="front-corner" viewBox="0 0 540 310" width="540" height="310" aria-hidden="true">
      <defs>
        <linearGradient id="curl-shade" x1="0" y1="0" x2="1" y2="1">
          <stop offset="0" stop-color="#2a2a2a"/>
          <stop offset="0.55" stop-color="#9a9a9a"/>
          <stop offset="1" stop-color="#ffffff"/>
        </linearGradient>
      </defs>
      <path d="M228,0 H540 V28 Q420,52 300,34 Q260,18 228,0 Z" fill="#1c1c1c"/>
      <path d="M300,34 Q420,52 540,28 V102 Q505,104 488,98 Q440,60 300,34 Z" fill="url(#curl-shade)"/>
    </svg>

    <div class="holder">
      <div class="holder-name">Your Name</div>
      <div class="holder-title">Title</div>
    </div>

    <div class="brand">
      <div class="brand-square"></div>
      <div>
        <div class="brand-name">HALVORN</div>
        <div class="brand-division">Trust Services</div>
      </div>
    </div>

    <ul class="contacts">
      <li>
        <svg class="contact-icon" viewBox="0 0 10 10"><path d="M2,1 L4,1 L4.5,3.5 L3.3,4.3 Q4.3,6 5.7,6.7 L6.5,5.5 L9,6 L9,8 Q8.5,9 7,9 Q1,8 1,2.5 Q1,1 2,1 Z" fill="#1a1a1a"/></svg>
        012-555-0148
      </li>
      <li>
        <svg class="contact-icon" viewBox="0 0 10 10"><circle cx="5" cy="3" r="2.2" fill="#1a1a1a"/><path d="M1,10 Q1,5.5 5,5.5 Q9,5.5 9,10 Z" fill="#1a1a1a"/></svg>
        012-555-0148
      </li>
      <li>
        <svg class="contact-icon" viewBox="0 0 10 10"><circle cx="5" cy="5" r="4.5" fill="#1a1a1a"/></svg>
        012-555-0148
      </li>
      <li>
        <svg class="contact-icon" viewBox="0 0 10 10"><rect x="0.5" y="0.5" width="9" height="9" fill="#1a1a1a"/></svg>
        012-555-0148
      </li>
      <li>
        <svg class="contact-icon" viewBox="0 0 10 10"><rect x="0.5" y="2" width="9" height="6.5" fill="none" stroke="#1a1a1a" stroke-width="1.2"/><path d="M0.5,2 L5,5.8 L9.5,2" fill="none" stroke="#1a1a1a" stroke-width="1.2"/></svg>
        inquiry@halvorngroup.com
      </li>
      <li>
        <svg class="contact-icon" viewBox="0 0 10 10"><circle cx="5" cy="5" r="4.3" fill="none" stroke="#1a1a1a" stroke-width="1.1"/><ellipse cx="5" cy="5" rx="1.9" ry="4.3" fill="none" stroke="#1a1a1a" stroke-width="0.9"/><path d="M0.7,5 H9.3" stroke="#1a1a1a" stroke-width="0.9"/></svg>
        www.halvorngroup.com
      </li>
    </ul>

    <div class="address">
      Street Name, City Name<br>
      Zip Code-00000
    </div>
  </section>

  <section class="card card-back" aria-label="Business card back">
    <div class="back-brand">
      <div class="back-square"></div>
      <span>HALVORN</span>
    </div>
    <div class="back-web">www.halvorngroup.com</div>
  </section>

</main>
</body>
</html>
```